Create Modern Clean Memorable Home Page

Please visit our current Homepage at www.brelvox.com. We want a fresh fun updated and memorable look. Feel free to use any of our photos if necessary. For more inspiration here are some other ice melt websites to browse:
http://www.quoralt.com/
http://www.pembrith.com/ice-melt/
http://www.globalvendrasalt.com/logistics.html
http://www.halvicsalt.com/
http://www.gubrine.com/
http://www.brinevaultco.com/gallery
http://www.thawfrost.com/products/calcium-chloride/
http://www.pelbranworks.com/dry-products
Updates
I have uploaded the logo
Just a note, we are not looking to simply display the product bags on the homepage. We want the first look at our page to pop and be memorable. We want color and possibly the use of photos with people and or animals and or landscapes to depict the use of the product. Most importantly it should be clean and not busy.
Industry/Entity Type
Logistics
Look and feel
Each slider illustrates characteristics of the customer's brand and the style your logo design should communicate.

```html
<!DOCTYPE html>
<html lang="en">
<head>
<meta charset="utf-8">
<title>Brelvox Seasonal Products, Inc. — Home</title>
<link rel="stylesheet" href="https://fonts.googleapis.com/css2?family=Tinos:wght@400;700&family=Arimo:wght@400;700&display=swap">
<style>
  :root {
    --navy: #1d4585;
    --navy-deep: #14304f;
    --nav-active: #5b77a9;
    --slate: #9aaac4;
    --panel: #ffffff;
    --panel-edge: #b9d3a8;
    --mission-red: #d9461b;
    --mission-blue: #1d3f7a;
    --accent-gold: #c07a3a;
    --button-brown: #9c6e3d;
    --login-title: #d8f0a8;
    --submit: #dcefb4;
    --logo-blue: #1a76b8;
  }
  * { box-sizing: border-box; margin: 0; padding: 0; }
  html, body { width: 1200px; height: 1000px; overflow: hidden; }
  body { position: relative; font-family: "Tinos", "Times New Roman", serif; }

  .backdrop {
    position: absolute; inset: 0;
    background:
      radial-gradient(ellipse at 8% 45%, #e9eef5 0%, rgba(233,238,245,0) 30%),
      radial-gradient(ellipse at 95% 45%, #e6ecf4 0%, rgba(230,236,244,0) 30%),
      linear-gradient(180deg, #2b5fa6 0%, #4d7fc0 20%, #a9bfdc 45%, #dfe6ef 70%, #eef2f7 100%);
  }

  .page {
    position: absolute; left: 127px; top: 24px; width: 962px; height: 948px;
    background: var(--panel); border: 2px solid var(--panel-edge); border-radius: 18px;
  }

  .abs { position: absolute; }

  .brand { left: 147px; top: 52px; display: flex; align-items: center; gap: 8px; }
  .brand-mark { width: 22px; height: 22px; background: var(--logo-blue); }
  .brand-name { font-family: "Arimo", Arial, sans-serif; font-size: 22px; color: var(--logo-blue); font-weight: 400; letter-spacing: -0.5px; }

  .mission { left: 155px; top: 147px; width: 320px; font-size: 13px; font-weight: 700; color: var(--mission-blue); line-height: 14px; }
  .mission .label { color: var(--mission-red); font-size: 14px; }
  .mission .indent { padding-left: 71px; }

  .photo { display: block; }
  .header-photo { left: 516px; top: 28px; width: 550px; height: 198px; border-radius: 12px;
    background: linear-gradient(180deg, #6c95c9 0%, #a8c2df 40%, #c9a25a 55%, #6a5a3a 75%, #e8edf2 100%); }

  .main-nav { left: 131px; top: 225px; width: 958px; height: 47px; background: var(--navy);
    box-shadow: 3px 4px 4px rgba(0,0,0,0.45); display: flex; align-items: center; }
  .nav-item { font-size: 11px; font-weight: 700; color: #fff; text-transform: uppercase; position: absolute; top: 0; height: 47px; line-height: 47px; }
  .nav-item.active { background: var(--nav-active); left: 2px; width: 101px; text-align: center; }

  .hero-photo { left: 146px; top: 276px; width: 652px; height: 222px; border-radius: 10px;
    background: linear-gradient(180deg, #1f4f9c 0%, #5c86c8 25%, #dfe8f4 45%, #b6c8e4 65%, #3f67ae 82%, #e6edf7 100%); }

  .login { left: 822px; top: 283px; width: 244px; height: 160px; background: var(--navy-deep); border-radius: 3px;
    font-family: "Arimo", Arial, sans-serif; color: #fff; }
  .login-title { position: absolute; top: 12px; width: 100%; text-align: center; font-weight: 700; font-size: 16px; color: var(--login-title); }
  .login-label { position: absolute; left: 21px; font-size: 13px; }
  .login-field { position: absolute; left: 21px; width: 198px; height: 17px; background: #fff; border: none; }
  .login-submit { position: absolute; left: 154px; top: 130px; width: 65px; height: 20px; background: var(--submit); border-radius: 4px;
    color: #000; font-size: 13px; text-align: center; line-height: 20px; }

  .card { position: absolute; }
  .card-body { position: absolute; color: #fff; }
  .card-title { position: absolute; left: 29px; font-size: 14px; font-weight: 700; }
  .card-sub { position: absolute; left: 29px; font-size: 14px; color: var(--accent-gold); }
  .card-text { position: absolute; left: 28px; width: 235px; font-size: 11.3px; line-height: 11px; }
  .read-more { position: absolute; width: 67px; height: 22px; background: var(--button-brown); color: #fff;
    font-size: 10px; text-align: center; line-height: 22px; box-shadow: 3px 3px 3px rgba(0,0,0,0.55); }

  .card-company { left: 148px; top: 507px; width: 295px; height: 453px; }
  .card-products { left: 458px; top: 512px; width: 289px; height: 450px; }
  .card-goal { left: 771px; top: 507px; width: 297px; height: 453px; }

  .footer-note { left: 0; width: 1200px; top: 981px; text-align: center; font-size: 10px; font-weight: 700; color: var(--mission-blue); }
</style>
</head>
<body>
  <div class="backdrop" role="img" aria-label="Snow-covered mountain range under a blue sky"></div>

  <div class="page"></div>

  <div class="abs brand">
    <span class="brand-mark"></span>
    <span class="brand-name">Brelvox seasonal products, inc.</span>
  </div>

  <p class="abs mission"><span class="label">OUR MISSION :</span> to become your supplier with a<br><span class="indent">quality product at a competitive price.</span></p>

  <div class="abs photo header-photo" role="img" aria-label="Wheel loader tipping ice melt salt into a dump truck"></div>

  <nav class="abs main-nav">
    <span class="nav-item active">Home</span>
    <span class="nav-item" style="left:126px">Copmany</span>
    <span class="nav-item" style="left:245px">Products</span>
    <span class="nav-item" style="left:362px">Order Online</span>
    <span class="nav-item" style="left:491px">Ice Melter Resource Center</span>
    <span class="nav-item" style="left:719px">News &amp; Press</span>
    <span class="nav-item" style="left:860px">Contact Us</span>
  </nav>

  <div class="abs photo hero-photo" role="img" aria-label="Snow-laden trees above a wide winter valley"></div>

  <form class="abs login">
    <div class="login-title">LOGIN</div>
    <div class="login-label" style="top:39px">Username:</div>
    <div class="login-field" style="top:57px"></div>
    <div class="login-label" style="top:81px">Password:</div>
    <div class="login-field" style="top:98px"></div>
    <div class="login-submit">Submit</div>
  </form>

  <section class="card card-company">
    <div class="abs photo" style="left:0;top:0;width:295px;height:176px;background:linear-gradient(180deg,#d9dde0 0%,#eef0ee 45%,#c8b07a 70%,#e9ecef 100%)" role="img" aria-label="Rack of snow shovels in a warehouse"></div>
    <div class="card-body" style="left:0;top:176px;width:295px;height:277px;background:var(--navy)">
      <h2 class="card-title" style="top:20px">Our Company</h2>
      <p class="card-sub" style="top:57px">Lorem Ipsum</p>
      <p class="card-text" style="top:84px">Lorem Ipsum is simply dummy text of the printing and typesetting industry.Lorem Ipsum is simply dummy text of the printing and typesetting industry.Lorem Ipsum is simply dummy text of the printing and typesetting ind ustry.Lorem Ipsum is simply dummy text of the printing and typesetting industry.Lorem Ipsum is simply dummy text of the printing and typesetting industry.Lorem Ipsum is simply dummy text of the printing and typesetting industry.Lorem Ipsum is simply dummy text of the printing and typesetting</p>
      <span class="read-more" style="left:190px;top:241px">Read More</span>
    </div>
  </section>

  <section class="card card-products">
    <div class="abs photo" style="left:0;top:0;width:289px;height:171px;background:#fff"></div>
    <div class="abs photo" style="left:2px;top:0;width:115px;height:171px;background:linear-gradient(180deg,#3a7fc4 0%,#bcd7ef 40%,#e6eef6 60%,#1b2f5a 100%)" role="img" aria-label="Bag of ice melter product"></div>
    <div class="abs photo" style="left:117px;top:0;width:172px;height:171px;background:linear-gradient(160deg,#ffffff 30%,#2b3f8c 60%,#ffffff 90%)" role="img" aria-label="Blue snow pusher shovel"></div>
    <div class="card-body" style="left:0;top:169px;width:289px;height:281px;background:var(--slate);color:#1a1a1a">
      <h2 class="card-title" style="top:23px;color:#1e2a44">Our Products</h2>
      <p class="card-sub" style="top:60px">Lorem Ipsum</p>
      <p class="card-text" style="top:87px">Lorem Ipsum is simply dummy text of the printing and typesetting industry.Lorem Ipsum is simply dummy text of the printing and typesetting industry.Lorem Ipsum is simply dummy text of the printing and typesetting ind ustry.Lorem Ipsum is simply dummy text of the printing and typesetting industry.Lorem Ipsum is simply dummy text of the printing and typesetting industry.Lorem Ipsum is simply dummy text of the printing and typesetting industry.Lorem Ipsum is simply dummy text of the printing and typesetting</p>
      <span class="read-more" style="left:191px;top:245px">Read More</span>
    </div>
  </section>

  <section class="card card-goal">
    <div class="abs photo" style="left:0;top:0;width:297px;height:171px;background:linear-gradient(135deg,#c9d6e8 0%,#eef3fa 50%,#b7c8e0 100%)" role="img" aria-label="Pencil writing a word on paper"></div>
    <div class="card-body" style="left:0;top:171px;width:297px;height:282px;background:var(--navy)">
      <h2 class="card-title" style="top:25px">Our goal</h2>
      <p class="card-sub" style="top:62px">Lorem Ipsum</p>
      <p class="card-text" style="top:89px">Lorem Ipsum is simply dummy text of the printing and typesetting industry.Lorem Ipsum is simply dummy text of the printing and typesetting industry.Lorem Ipsum is simply dummy text of the printing and typesetting ind ustry.Lorem Ipsum is simply dummy text of the printing and typesetting industry.Lorem Ipsum is simply dummy text of the printing and typesetting industry.Lorem Ipsum is simply dummy text of the printing and typesetting industry.Lorem Ipsum is simply dummy text of the printing and typesetting</p>
      <span class="read-more" style="left:191px;top:246px">Read More</span>
    </div>
  </section>

  <p class="abs footer-note">Copyright @ 2013. All rights reserved</p>
</body>
</html>
```